Bref créative
Corvale Power Associates, LLC
Stationery and business cards
Professional
Dean Halvorsen
President
28715 Birchwood Crest Lane
Suite 615
Houston, TX 77084
dean.halvorsen@corvale-pa.com
We will need multiple name, cell phone, and email changes. Primary colors should be white, black, and a vibrant blue.
Here is our logo Ai.

```html
<!DOCTYPE html>
<html lang="en">
<head>
<meta charset="utf-8">
<title>Corvale Power Associates — Stationery</title>
<link rel="stylesheet" href="https://fonts.googleapis.com/css2?family=Montserrat:wght@600&family=Open+Sans:wght@400;600&display=swap">
<style>
  :root {
    --stage: #3d7a28;
    --paper: #ffffff;
    --paper-edge: #c9ccd0;
    --flap-line: #d6d9dc;
    --brand-blue: #1b8fd2;
    --accent-dark: #3a3f44;
    --ink: #2b2f33;
    --ink-soft: #6b7076;
    --shadow: rgba(0, 0, 0, 0.45);
  }
  * { margin: 0; padding: 0; box-sizing: border-box; }
  html, body { width: 1200px; height: 671px; overflow: hidden; }
  body { background: var(--stage); font-family: "Open Sans", Arial, sans-serif; color: var(--ink); position: relative; }

  .sheet {
    position: absolute;
    background: var(--paper);
    border: 1px solid var(--paper-edge);
    box-shadow: 0 3px 10px var(--shadow), 0 0 2px var(--shadow);
    overflow: hidden;
  }
  .letterhead { left: 209px; top: 34px; width: 451px; height: 588px; z-index: 1; }
  .business-card { left: 67px; top: 283px; width: 192px; height: 113px; z-index: 3; }
  .envelope-back { left: 619px; top: 120px; width: 475px; height: 204px; z-index: 2; }
  .envelope-front { left: 619px; top: 348px; width: 475px; height: 209px; z-index: 2; }

  .brand { position: absolute; display: flex; align-items: center; gap: 6px; }
  .brand-mark { width: 10px; height: 10px; border-radius: 50%; background: var(--brand-blue); }
  .brand-name { font-family: "Montserrat", Arial, sans-serif; font-weight: 600; color: var(--brand-blue); letter-spacing: 1px; text-transform: uppercase; }
  .brand-tagline { font-family: "Montserrat", Arial, sans-serif; font-weight: 600; color: var(--brand-blue); text-transform: uppercase; letter-spacing: 1px; position: absolute; white-space: nowrap; }

  .letterhead .brand { left: 28px; top: 34px; }
  .letterhead .brand-name { font-size: 14px; }
  .letterhead .brand-tagline { left: 44px; top: 55px; font-size: 5px; }

  .envelope-front .brand { left: 140px; top: 30px; }
  .envelope-front .brand-name { font-size: 13px; }
  .envelope-front .brand-tagline { left: 156px; top: 50px; font-size: 5px; }

  .business-card .brand { left: 10px; top: 18px; gap: 4px; }
  .business-card .brand-mark { width: 6px; height: 6px; }
  .business-card .brand-name { font-size: 8px; }
  .business-card .brand-tagline { left: 20px; top: 31px; font-size: 3.5px; }

  .contact { position: absolute; font-size: 6px; line-height: 1.5; color: var(--ink-soft); white-space: nowrap; }
  .letterhead .phones { left: 28px; bottom: 24px; }
  .letterhead .address { left: 300px; bottom: 18px; }
  .envelope-front .phones { left: 232px; top: 34px; border-left: 1px solid var(--flap-line); padding-left: 6px; }
  .business-card .holder { left: 98px; top: 12px; font-size: 5px; color: var(--ink); }
  .business-card .holder b { font-weight: 600; }
  .business-card .phones { left: 10px; top: 92px; font-size: 4px; }
  .business-card .address { left: 98px; top: 84px; font-size: 4px; }

  .accent { position: absolute; height: 3px; }
  .accent.blue { background: var(--brand-blue); }
  .accent.dark { background: var(--accent-dark); }
  .accent.v { width: 3px; }

  .flap { position: absolute; inset: 0; }
</style>
</head>
<body>

<section class="sheet letterhead" aria-label="Letterhead">
  <div class="brand"><span class="brand-mark"></span><span class="brand-name">Corvale</span></div>
  <div class="brand-tagline">Power Associates</div>

  <span class="accent blue" style="right:6px;top:0;width:16px"></span>
  <span class="accent dark v" style="right:0;top:0;height:22px"></span>
  <span class="accent blue v" style="left:0;bottom:40px;height:16px"></span>
  <span class="accent dark" style="left:0;bottom:0;width:26px"></span>
  <span class="accent blue" style="right:10px;bottom:0;width:22px"></span>

  <div class="contact phones">P: 281-555-0142<br>C: 832-555-0187</div>
  <div class="contact address">E: dean.halvorsen@corvale-pa.com<br>28715 Birchwood Crest Lane<br>Suite 615 · Houston, TX 77084</div>
</section>

<section class="sheet business-card" aria-label="Business card">
  <div class="brand"><span class="brand-mark"></span><span class="brand-name">Corvale</span></div>
  <div class="brand-tagline">Power Associates</div>
  <div class="contact holder"><b>Dean Halvorsen</b> | President</div>
  <span class="accent blue v" style="left:0;top:0;height:14px"></span>
  <span class="accent dark" style="right:0;bottom:0;width:18px"></span>
  <div class="contact phones">P: 281-555-0142<br>C: 832-555-0187</div>
  <div class="contact address">E: dean.halvorsen@corvale-pa.com<br>28715 Birchwood Crest Lane<br>Suite 615, Houston, TX 77084</div>
</section>

<section class="sheet envelope-back" aria-label="Envelope back">
  <svg class="flap" width="475" height="204" viewBox="0 0 475 204">
    <polyline points="0,2 18,72 457,72 475,2" fill="none" stroke="var(--flap-line)" stroke-width="1.2"/>
  </svg>
</section>

<section class="sheet envelope-front" aria-label="Envelope front">
  <div class="brand"><span class="brand-mark"></span><span class="brand-name">Corvale</span></div>
  <div class="brand-tagline">Power Associates</div>
  <div class="contact phones">P: 281-555-0142<br>C: 832-555-0187</div>
  <span class="accent blue" style="right:8px;top:0;width:18px"></span>
  <span class="accent dark v" style="right:0;top:0;height:20px"></span>
  <span class="accent blue v" style="left:0;top:120px;height:18px"></span>
  <span class="accent dark" style="left:0;bottom:0;width:24px"></span>
</section>

</body>
</html>
```